Letterhead Design Project

Letterhead for a Consultant Cardiologist in Adelaide Australia. Should be very classy, mature and imposing. I would prefer colours that portray confidence, gentleness and serenity.

The PDF attached is for you to see the details that will be on the letterhead and not the design which is extremely poor!

Target Market(s)

Health professionals especially medical doctors

Industry/Entity Type

Consultant

```html
<!DOCTYPE html>
<html lang="en">
<head>
<meta charset="utf-8">
<title>Letterhead – Dr. Ifeanyi R. Okafor, Cardiologist</title>
<link rel="stylesheet" href="https://fonts.googleapis.com/css2?family=Open+Sans:wght@600;700&family=Cinzel:wght@400;700&display=swap">
<style>
  :root {
    --slate: #4a5f73;
    --sky: #6ccaf0;
    --teal: #1f7ea1;
    --ink: #1e1e1e;
    --paper: #ffffff;
  }
  html, body { margin: 0; padding: 0; overflow: hidden; }
  body { width: 928px; height: 1200px; background: var(--paper); position: relative; }
  .letterhead { position: relative; width: 928px; height: 1200px; overflow: hidden; }

  .sidebar { position: absolute; left: 0; top: 0; width: 187px; height: 1024px; background: var(--slate); }

  .identity {
    position: absolute; left: 82px; top: 492px;
    transform: rotate(-90deg); transform-origin: left top;
    white-space: nowrap;
  }
  .doctor-name {
    font-family: "Open Sans", sans-serif; font-weight: 700;
    font-size: 30px; line-height: 34px; color: var(--paper); letter-spacing: -0.2px;
  }
  .role-line { display: flex; align-items: center; gap: 6px; margin-top: -1px; }
  .specialty {
    font-family: "Cinzel", serif; font-weight: 400; font-size: 23px; line-height: 26px;
    color: var(--sky); letter-spacing: 0.5px;
  }
  .divider { width: 1px; height: 22px; background: var(--paper); }
  .credentials {
    font-family: "Cinzel", serif; font-weight: 700; font-size: 12px;
    color: var(--paper); word-spacing: 6px; letter-spacing: 0.4px;
  }
  .brand-dot {
    position: absolute; left: 80px; top: 502px; width: 68px; height: 68px;
    border-radius: 50%; background: var(--sky);
  }

  .footer-label {
    position: absolute; left: 162px; top: 1186px;
    transform: rotate(-90deg); transform-origin: left top;
    font-family: "Open Sans", sans-serif; font-weight: 700; font-size: 28px;
    line-height: 30px; color: var(--slate); white-space: nowrap;
  }
  .location { position: absolute; top: 1050px; }
  .location.primary { left: 207px; }
  .location.regional { left: 500px; }
  .location.metro { left: 682px; }
  .location h2 {
    margin: 0; font-family: "Open Sans", sans-serif; font-weight: 700;
    font-size: 14px; line-height: 16px; color: var(--teal);
  }
  .location p {
    margin: 0; font-family: "Cinzel", serif; font-weight: 700;
    font-size: 12px; line-height: 16.3px; color: var(--ink); white-space: nowrap;
  }
</style>
</head>
<body>
<main class="letterhead">
  <aside class="sidebar">
    <div class="identity">
      <div class="doctor-name">Dr. Ifeanyi R. Okafor</div>
      <div class="role-line">
        <span class="specialty">CARDIOLOGIST</span>
        <span class="divider"></span>
        <span class="credentials">M.B.B.S F.M.C.P F.R.A.C.P</span>
      </div>
    </div>
    <div class="brand-dot"></div>
  </aside>

  <div class="footer-label">Consultant</div>

  <section class="location primary">
    <h2>Northgate Heart &amp; Specialist Clinic</h2>
    <h2>Meridian Central Private Hospital</h2>
    <p>18-24 Harlow Road</p>
    <p>Elmwood Vale SA 5120</p>
    <p>T: 8201 4470</p>
    <p>F: 8201 4471</p>
    <p>E: heart@northgateclinic.com.au</p>
    <p>Provider No: 512840KK</p>
  </section>

  <section class="location regional">
    <h2>Port Hallett Hospital</h2>
    <p>46 Infirmary Road</p>
    <p>Port Hallett 5710</p>
    <p>T: 8641 2200</p>
    <p>F: 8641 2201</p>
    <p>Provider No: 512840UB</p>
  </section>

  <section class="location metro">
    <h2>The Linden Specialist Centre</h2>
    <p>52 Kingsley Road</p>
    <p>Kingsley South SA 5014</p>
    <p>T: 8247 3390</p>
    <p>F: 8247 3391</p>
    <p>Provider No: 512840LY</p>
  </section>
</main>
</body>
</html>
```